Counseling business card, clean but alluring

I need it to appeal to all ages and men. I’m planning to use my current logo. I like crisp and clean. Possibly some shimmer. My website is harborleafwellness.net

Contact Information for Business Card

Marissa "Missy" Dolan Pryce, LPC, RPT

harborleafwellness.net

28159 Larkspur Avenue, Suite 407
Addison TX 75094

469-315-2984 | missy@harborleafwellness.net

Colors
0355a3
85cae6
fbee3e
ffffff
33b8a4
0692cd

Requirements
Must have
• My logo

```html
<!DOCTYPE html>
<html lang="en">
<head>
<meta charset="utf-8">
<title>Harborleaf Wellness – Business Card</title>
<link rel="stylesheet" href="https://fonts.googleapis.com/css2?family=Tenor+Sans&family=Lato:wght@300;400&display=swap">
<style>
  :root {
    --page-bg: #eef0f3;
    --card-bg: #ffffff;
    --brand-blue: #3f73c8;
    --soft-blue: #7ea6e0;
    --pale-blue: #c9daf3;
    --ring-grey: #e4e6ea;
    --text-grey: #555a60;
  }
  * { box-sizing: border-box; margin: 0; padding: 0; }
  html, body {
    width: 1200px; height: 1200px; overflow: hidden;
    background: var(--page-bg);
  }
  .sheet { position: relative; width: 1200px; height: 1200px; }
  .card {
    position: absolute; left: 130px; width: 940px; height: 537px;
    background: var(--card-bg); overflow: hidden;
    box-shadow: 0 18px 30px rgba(0,0,0,0.12);
  }
  .card--front { top: 43px; }
  .card--back { top: 620px; }
  .card__decor { position: absolute; inset: 0; width: 940px; height: 537px; }

  .brand {
    position: absolute; display: flex; align-items: center;
    font-family: "Tenor Sans", sans-serif; color: var(--brand-blue);
    white-space: nowrap;
  }
  .brand__dot { border-radius: 50%; background: var(--soft-blue); flex: none; }
  .card--front .brand { left: 100px; top: 370px; font-size: 60px; gap: 24px; }
  .card--front .brand__dot { width: 46px; height: 46px; }
  .card--back .brand { right: 60px; bottom: 62px; font-size: 30px; gap: 12px; }
  .card--back .brand__dot { width: 24px; height: 24px; }

  .holder { position: absolute; left: 78px; top: 84px; font-family: "Lato", sans-serif; }
  .holder__name { font-size: 27px; font-weight: 400; color: var(--soft-blue); }
  .holder__name small { font-size: 18px; color: var(--text-grey); margin-left: 6px; }
  .holder__title { font-size: 15px; color: var(--text-grey); margin-top: 4px; }

  .contacts {
    position: absolute; left: 68px; top: 218px; list-style: none;
    font-family: "Lato", sans-serif; font-weight: 300; font-size: 23px;
    color: var(--text-grey); line-height: 30px;
  }
  .contacts li { display: flex; gap: 14px; margin-bottom: 28px; }
  .contacts svg { flex: none; width: 26px; height: 26px; margin-top: 2px; }
</style>
</head>
<body>
<main class="sheet">

  <section class="card card--front">
    <svg class="card__decor" viewBox="0 0 940 537">
      <defs>
        <radialGradient id="vineFill" cx="0.6" cy="0.5" r="0.6">
          <stop offset="0" stop-color="#dbe6f7"/>
          <stop offset="1" stop-color="#8fb1e4"/>
        </radialGradient>
      </defs>
      <circle cx="770" cy="110" r="262" fill="none" stroke="var(--ring-grey)" stroke-width="3"/>
      <circle cx="762" cy="100" r="252" fill="none" stroke="var(--soft-blue)" stroke-width="2"/>
      <circle cx="800" cy="100" r="205" fill="url(#vineFill)" opacity="0.75"
              role="img" aria-label="Circular wreath of leafy blue vines"/>
    </svg>
    <div class="brand"><span class="brand__dot"></span>Harborleaf Wellness</div>
  </section>

  <section class="card card--back">
    <svg class="card__decor" viewBox="0 0 940 537">
      <defs>
        <radialGradient id="vineFillBack" cx="0.6" cy="0.5" r="0.6">
          <stop offset="0" stop-color="#dbe6f7"/>
          <stop offset="1" stop-color="#8fb1e4"/>
        </radialGradient>
      </defs>
      <circle cx="775" cy="110" r="250" fill="none" stroke="var(--ring-grey)" stroke-width="3"/>
      <circle cx="768" cy="100" r="240" fill="none" stroke="var(--soft-blue)" stroke-width="2"/>
      <circle cx="800" cy="105" r="200" fill="url(#vineFillBack)" opacity="0.75"
              role="img" aria-label="Circular wreath of leafy blue vines"/>
    </svg>

    <div class="holder">
      <p class="holder__name">Marissa Dolan Pryce<small>LPC, RPT</small></p>
      <p class="holder__title">Counselor and Registered Play Therapist.</p>
    </div>

    <ul class="contacts">
      <li>
        <svg viewBox="0 0 26 26"><circle cx="13" cy="13" r="12" fill="var(--soft-blue)"/>
          <path d="M9 7l3 3-2 2c1 2 2 3 4 4l2-2 3 3-2 2c-5 0-10-5-10-10z" fill="#fff"/></svg>
        <span>469-315-2984</span>
      </li>
      <li>
        <svg viewBox="0 0 26 26"><circle cx="13" cy="13" r="12" fill="var(--soft-blue)"/>
          <circle cx="13" cy="13" r="7" fill="none" stroke="#fff" stroke-width="1.5"/>
          <path d="M6 13h14M13 6c-3 4-3 10 0 14M13 6c3 4 3 10 0 14" fill="none" stroke="#fff" stroke-width="1.3"/></svg>
        <span>missy@harborleafwellness.net<br>www.harborleafwellness.net</span>
      </li>
      <li>
        <svg viewBox="0 0 26 26"><circle cx="13" cy="13" r="12" fill="var(--soft-blue)"/>
          <circle cx="13" cy="13" r="6" fill="#fff"/><circle cx="13" cy="13" r="3" fill="var(--soft-blue)"/></svg>
        <span>28159 Larkspur Avenue<br>Suite 407 Addison TX<br>75094</span>
      </li>
    </ul>

    <div class="brand"><span class="brand__dot"></span>Harborleaf Wellness</div>
  </section>

</main>
</body>
</html>
```